new roofing company card

New primary business card for roofing company.

Industry/Entity Type

Residential roofing/Specializing in Asphalt and Standing seam metal roofing

Contact Information for Business Card

Phone number is: 484 672 1058 Email: support@fennridgeroofworks.com website: www.fennridgeroofworks.com

Colors
EB3D1F
EC4F4E
F09395
F8D3D4
FCEDEE

```html
<!DOCTYPE html>
<html lang="en">
<head>
<meta charset="utf-8">
<title>Fennridge Roofworks – Business Card</title>
<link rel="stylesheet" href="https://fonts.googleapis.com/css2?family=Open+Sans:wght@400;600;700;800&display=swap">
<style>
  :root {
    --stage: #1c1c1c;
    --card-dark: #2a2b2a;
    --card-light: #ffffff;
    --ink: #1f1f1f;
    --red: #c9302c;
    --silver: #b9b9b9;
  }
  html, body {
    margin: 0;
    padding: 0;
    width: 1200px;
    height: 977px;
    overflow: hidden;
    background: var(--stage);
    font-family: "Open Sans", Arial, sans-serif;
  }
  .canvas {
    position: relative;
    width: 1200px;
    height: 977px;
  }
  .card {
    position: absolute;
    width: 540px;
    height: 310px;
    border-radius: 18px;
    overflow: hidden;
  }
  .card--back {
    left: 100px;
    top: 140px;
    background: var(--card-dark);
    display: flex;
    align-items: center;
    justify-content: center;
  }
  .back-wordmark {
    display: flex;
    align-items: center;
    gap: 14px;
  }
  .back-wordmark .mark-square {
    width: 30px;
    height: 30px;
    background: var(--red);
  }
  .back-wordmark .mark-name {
    font-weight: 700;
    font-size: 28px;
    letter-spacing: 2px;
    color: var(--silver);
    line-height: 1;
  }

  .card--front {
    left: 560px;
    top: 520px;
    background: var(--card-light);
  }
  .front-band {
    position: absolute;
    left: 0;
    right: 0;
    bottom: 0;
    height: 54px;
    background: var(--card-dark);
  }
  .front-decor {
    position: absolute;
    right: -40px;
    top: 28px;
    width: 200px;
    height: 200px;
    background: var(--red);
  }
  .front-content {
    position: absolute;
    left: 36px;
    top: 34px;
  }
  .wordmark {
    display: flex;
    align-items: center;
    gap: 10px;
    margin-bottom: 22px;
  }
  .wordmark .mark-square {
    width: 22px;
    height: 22px;
    background: var(--red);
  }
  .wordmark .mark-name {
    font-weight: 700;
    font-size: 22px;
    letter-spacing: 1.5px;
    color: var(--ink);
    line-height: 1;
  }
  .person-name {
    margin: 0;
    font-weight: 800;
    font-size: 22px;
    letter-spacing: 0.5px;
    color: var(--ink);
    text-transform: uppercase;
  }
  .person-role {
    margin: 2px 0 16px;
    font-size: 14px;
    color: var(--red);
  }
  .contact-list {
    list-style: none;
    margin: 0;
    padding: 0;
  }
  .contact-list li {
    display: flex;
    align-items: center;
    gap: 9px;
    font-size: 13px;
    color: var(--ink);
    margin-bottom: 5px;
  }
  .contact-icon {
    width: 16px;
    height: 16px;
    flex: none;
  }
</style>
</head>
<body>
<main class="canvas">

  <section class="card card--back" aria-label="Card back">
    <div class="back-wordmark">
      <span class="mark-square"></span>
      <span class="mark-name">FENNRIDGE ROOFWORKS</span>
    </div>
  </section>

  <section class="card card--front" aria-label="Card front">
    <div class="front-decor"></div>
    <div class="front-band"></div>

    <div class="front-content">
      <div class="wordmark">
        <span class="mark-square"></span>
        <span class="mark-name">FENNRIDGE ROOFWORKS</span>
      </div>

      <h1 class="person-name">Daniel Harper</h1>
      <p class="person-role">Founder &amp; CEO</p>

      <ul class="contact-list">
        <li>
          <svg class="contact-icon" viewBox="0 0 16 16" aria-hidden="true">
            <circle cx="8" cy="8" r="8" fill="var(--red)"/>
            <path d="M5.2 4.2l1.4-.4.9 2-1 .7c.4.9 1.1 1.6 2 2l.7-1 2 .9-.4 1.4c-3 .2-5.8-2.6-5.6-5.6z" fill="#fff"/>
          </svg>
          484 672 1058
        </li>
        <li>
          <svg class="contact-icon" viewBox="0 0 16 16" aria-hidden="true">
            <circle cx="8" cy="8" r="8" fill="var(--red)"/>
            <rect x="4" y="5" width="8" height="6" rx="0.8" fill="#fff"/>
            <path d="M4.3 5.4L8 8.3l3.7-2.9" stroke="var(--red)" stroke-width="0.9" fill="none"/>
          </svg>
          support@fennridgeroofworks.com
        </li>
        <li>
          <svg class="contact-icon" viewBox="0 0 16 16" aria-hidden="true">
            <circle cx="8" cy="8" r="8" fill="var(--red)"/>
            <circle cx="8" cy="8" r="4" stroke="#fff" stroke-width="1" fill="none"/>
            <path d="M4 8h8M8 4c-1.6 2.2-1.6 5.8 0 8M8 4c1.6 2.2 1.6 5.8 0 8" stroke="#fff" stroke-width="0.8" fill="none"/>
          </svg>
          www.fennridgeroofworks.com
        </li>
      </ul>
    </div>
  </section>

</main>
</body>
</html>
```